Company Website for an IT business called "BRIGHT CORRIDOR"

Complete website creation with text and graphics.
We need :
- modern and creative design for our IT company
- Content management system to edit text later on
- Integrate third party content from partner company
- Contact form (transfer by email)
Updates

Designs look the same

Target Market(s)

Small and medium business
private customers

Industry/Entity Type

Information Technology

Coding

Coded - Design and coding required

Number of Pages Required

1 page

Font styles to use
Sans Serif

Requirements
Must have
• Contact form
Link to legal information
Link to data protection (GDPR)
Link to website owner declaration
Nice to have
• Fresh and creative graphics for IT business

```html
<!DOCTYPE html>
<html lang="en">
<head>
<meta charset="utf-8">
<title>BRIGHT CORRIDOR – Outsourced IT Services</title>
<link href="https://fonts.googleapis.com/css2?family=Poppins:wght@400;500;600;700;800&display=swap" rel="stylesheet">
<style>
:root{
  --blue:#0f9ad8;
  --blue-light:#74c8ee;
  --blue-pale:#e3f3fb;
  --ink:#2f2f2f;
  --text:#666;
  --muted:#9a9a9a;
  --dark:#3d3d3d;
  --footer:#424242;
  --field:#f0f0f0;
  --white:#fff;
}
*{margin:0;padding:0;box-sizing:border-box}
html,body{width:1200px;height:4815px;overflow:hidden}
body{font-family:'Poppins',sans-serif;color:var(--ink);background:var(--white);position:relative}
.abs{position:absolute}
a{color:inherit;text-decoration:none}
.btn{position:absolute;display:flex;align-items:center;justify-content:center;border-radius:20px;background:var(--blue);color:var(--white);font-size:11px;font-weight:700;letter-spacing:.4px;text-transform:uppercase}
.eyebrow{font-size:12px;color:var(--muted);letter-spacing:.6px;text-transform:uppercase}
.h2{font-size:34px;font-weight:700;line-height:1.2;color:var(--ink);letter-spacing:.3px}
.para{font-size:14.5px;line-height:24px;color:var(--text)}

/* header */
.site-header{position:absolute;top:0;left:0;width:1200px;height:88px;background:var(--white);z-index:5}
.brand{position:absolute;left:88px;top:28px;display:flex;align-items:center;gap:10px;font-size:21px;font-weight:600;color:var(--ink);letter-spacing:.5px}
.brand-mark{width:14px;height:14px;background:var(--blue)}
.main-nav{position:absolute;left:411px;top:36px;display:flex;gap:24px;font-size:12.5px;font-weight:500;color:var(--ink)}
.estimate{left:977px;top:26px;width:133px;height:36px;font-size:11px}

/* cards */
.card{position:absolute;background:var(--white);border-radius:8px;box-shadow:0 8px 24px rgba(0,0,0,.08);overflow:hidden}
.card-media{height:174px}
.card-body{padding:16px 20px}
.card-title{font-size:17px;font-weight:700;color:var(--ink);margin-top:12px}
.card-text{font-size:11.5px;line-height:20px;color:var(--text);margin-top:8px}
.card-meta{font-size:10px;color:var(--muted);margin-top:10px}
.card-meta b{color:var(--text);font-weight:500}
.post-title{font-size:17px;font-weight:700;line-height:21px;color:var(--ink);margin-top:8px}

/* form */
.label{position:absolute;font-size:11px;font-weight:600;color:var(--ink)}
.field{position:absolute;background:var(--field);font-size:12px;color:var(--muted);padding:0 18px;display:flex;align-items:center}

/* footer */
.foot-h{position:absolute;font-size:18px;font-weight:700;color:var(--white)}
.foot-list{position:absolute;list-style:none;font-size:12px;color:var(--white);line-height:26.5px}
.foot-text{position:absolute;font-size:12px;color:var(--white);line-height:20px}
.social{position:absolute;top:4635px;width:32px;height:32px;border-radius:50%;background:#555}
.bottom-bar{position:absolute;top:4780px;font-size:11px;color:var(--white);font-weight:500}
</style>
</head>
<body>

<header class="site-header">
  <div class="brand"><span class="brand-mark"></span>BRIGHT CORRIDOR</div>
  <nav class="main-nav">
    <a href="#">HOME</a><a href="#">ABOUT US</a><a href="#">SERVICES</a><a href="#">PROJECTS</a><a href="#">CASE STUDIES</a><a href="#">CONTACT US</a>
  </nav>
  <a class="btn estimate" href="#">Free Estimate</a>
</header>

<!-- hero -->
<section class="hero abs" style="left:0;top:88px;width:1200px;height:700px">
  <svg class="abs" width="1200" height="700" viewBox="0 0 1200 700" role="img" aria-label="Photo of two colleagues reviewing a document in an office">
    <defs>
      <linearGradient id="heroPhoto" x1="0" y1="0" x2="1" y2="1">
        <stop offset="0" stop-color="#4a4d52"/>
        <stop offset=".55" stop-color="#6c6f73"/>
        <stop offset="1" stop-color="#a7a9ac"/>
      </linearGradient>
      <linearGradient id="heroBlob" x1="0" y1="0" x2="1" y2="1">
        <stop offset="0" stop-color="#74c8ee"/>
        <stop offset="1" stop-color="#2e8fb8"/>
      </linearGradient>
    </defs>
    <rect width="1200" height="654" fill="url(#heroPhoto)"/>
    <path d="M0,540 C90,520 170,660 330,654 C470,648 560,610 660,600 C720,594 760,640 800,654 L0,654 Z" fill="#fff"/>
    <path d="M0,654 L1200,654 L1200,700 L0,700 Z" fill="#fff"/>
    <path d="M1200,360 C1130,370 1060,420 1020,480 C980,545 960,610 1010,670 C1070,720 1160,720 1200,700 Z" fill="url(#heroBlob)"/>
  </svg>
  <h1 class="abs" style="left:88px;top:168px;font-size:62px;font-weight:800;line-height:63px;color:var(--white);letter-spacing:1px">We Provide<br>Outsourced IT<br>Services</h1>
  <p class="abs" style="left:88px;top:368px;font-size:17px;font-weight:600;color:var(--white)">For Start-ups &amp; Mid-sized companies</p>
  <a class="btn" href="#" style="left:88px;top:413px;width:133px;height:34px">Get in touch</a>
</section>

<!-- who we are -->
<section class="about">
  <svg class="abs" style="left:0;top:807px" width="580" height="540" viewBox="0 0 580 540">
    <path d="M0,40 C120,0 330,-20 450,30 C560,80 590,250 560,380 C530,500 470,540 420,530 C300,510 120,450 0,420 Z" fill="var(--blue-pale)"/>
    <path d="M0,55 C110,20 300,20 400,50 C500,90 540,230 520,350 C500,460 460,530 420,530 C300,520 120,470 0,440 Z" fill="#8a8d91" role="img" aria-label="Photo of a team giving each other a high five over a desk"/>
  </svg>
  <p class="eyebrow abs" style="left:680px;top:916px">Who we are</p>
  <h2 class="h2 abs" style="left:680px;top:938px">Custom IT solution for<br>your business</h2>
  <p class="para abs" style="left:680px;top:1030px;width:425px">Aenean sollicitudin, lorem quis bibendum auctor, nisi elit consequat ipsum nec sagittis sem nibh id elit. Morbi accumsan ipsum velit. Nam nec tellus a odio tincidunt auctor a ornare odio. Sed non &nbsp;mauris vitae erat consequat auctor eu in elit. Class aptent taciti sociosqu ad litora torquent per conubia nostra, per inceptos himenaeos mauris in erat justo...</p>
  <a class="btn" href="#" style="left:680px;top:1226px;width:133px;height:34px">Learn more</a>
</section>

<!-- dark band -->
<svg class="abs" style="left:0;top:1860px" width="1200" height="900" viewBox="0 0 1200 900">
  <defs>
    <linearGradient id="darkBand" x1="0" y1="0" x2="1" y2="0">
      <stop offset="0" stop-color="#363636"/>
      <stop offset="1" stop-color="#6e6e6e"/>
    </linearGradient>
  </defs>
  <path d="M0,170 C200,30 380,0 560,60 C750,120 900,40 1200,40 L1200,700 C1130,760 1020,770 920,700 C820,640 720,640 620,700 C500,780 330,790 180,740 C100,710 40,700 0,700 Z" fill="url(#darkBand)"/>
  <path d="M700,160 C820,110 1000,120 1200,180 L1200,680 C1130,740 1030,740 940,690 C840,630 760,600 690,600 Z" fill="#8b8b8b" role="img" aria-label="Photo of a smiling man with glasses looking at his phone"/>
  <path d="M1200,0 C1110,0 1020,50 990,130 C970,190 1020,230 1100,240 C1150,245 1180,250 1200,260 Z" fill="#4fb1df"/>
  <path d="M0,540 C60,520 100,560 120,600 C150,680 200,730 160,790 C120,840 60,845 0,830 Z" fill="#3a9fcf"/>
</svg>
<section class="idea">
  <h2 class="h2 abs" style="left:185px;top:2088px;color:var(--white);font-size:34px">If you have the idea we<br>will find the right way</h2>
  <p class="para abs" style="left:185px;top:2186px;width:430px;color:#eee">Aenean sollicitudin, lorem quis bibendum auctor, nisi elit consequat ipsum nec sagittis sem nibh id elit. Morbi accumsan ipsum velit. Nam nec tellus a odio tincidunt auctor a ornare odio...</p>
  <a class="btn" href="#" style="left:185px;top:2310px;width:250px;height:39px">View all available positions</a>
</section>

<!-- services -->
<section class="services">
  <p class="eyebrow abs" style="left:0;top:1436px;width:1200px;text-align:center">Our services</p>
  <h2 class="h2 abs" style="left:0;top:1458px;width:1200px;text-align:center">Data analytics content &amp; IT<br>managed services</h2>
  <article class="card" style="left:213px;top:1566px;width:245px;height:335px">
    <div class="card-media" style="background:linear-gradient(135deg,#6f7276,#bfc1c3)" role="img" aria-label="Photo of colleagues discussing analytics at a desk"></div>
    <div class="card-body"><h3 class="card-title">Advanced Analytics</h3><p class="card-text">Nisi elit consequat ipsum nec sagittis sem nibh id elit. Duis sed odio sit amet nibh...</p></div>
  </article>
  <article class="card" style="left:477px;top:1566px;width:244px;height:335px">
    <div class="card-media" style="background:linear-gradient(135deg,#8c8f92,#d2d3d4)" role="img" aria-label="Photo of two coworkers looking at a tablet"></div>
    <div class="card-body"><h3 class="card-title">Content Management</h3><p class="card-text">Nisi elit consequat ipsum nec sagittis sem nibh id elit. Duis sed odio sit amet nibh...</p></div>
  </article>
  <article class="card" style="left:740px;top:1566px;width:245px;height:335px">
    <div class="card-media" style="background:linear-gradient(135deg,#a9abad,#e6e6e6)" role="img" aria-label="Photo of a woman holding a coffee cup"></div>
    <div class="card-body"><h3 class="card-title">Integrate Third Party</h3><p class="card-text">Nisi elit consequat ipsum nec sagittis sem nibh id elit. Duis sed odio sit amet nibh...</p></div>
  </article>
</section>

<!-- innovation -->
<section class="innovation">
  <svg class="abs" style="left:168px;top:2654px" width="400" height="460" viewBox="0 0 400 460">
    <path d="M0,350 C20,300 80,290 120,260 C200,200 330,220 380,280 C420,340 330,390 240,400 C150,410 40,420 0,350 Z" fill="#3f7fd0"/>
    <path d="M120,110 C160,60 250,40 300,120 L310,450 L110,450 Z" fill="#5f6266" role="img" aria-label="Photo of a bearded man in a blazer using a tablet"/>
  </svg>
  <h2 class="h2 abs" style="left:611px;top:2754px">Be at the forefront of<br>the new innovation</h2>
  <p class="para abs" style="left:611px;top:2852px;width:425px">Aenean sollicitudin, lorem quis bibendum auctor, nisi elit consequat ipsum nec sagittis sem nibh id elit. Morbi accumsan ipsum velit. Nam nec tellus a odio tincidunt auctor a ornare odio...</p>
  <a class="btn" href="#" style="left:611px;top:2975px;width:251px;height:42px">View all available positions</a>
</section>

<!-- articles -->
<section class="articles">
  <svg class="abs" style="left:900px;top:3045px" width="300" height="250" viewBox="0 0 300 250">
    <path d="M300,0 C220,0 140,30 90,90 C40,150 60,230 130,245 C200,255 260,240 300,230 Z" fill="var(--blue-light)"/>
  </svg>
  <h2 class="h2 abs" style="left:0;top:3152px;width:1200px;text-align:center;font-size:31px">Latest Articles</h2>
  <article class="card" style="left:213px;top:3215px;width:245px;height:360px">
    <div class="card-media" style="background:linear-gradient(135deg,#6b6e72,#c6c7c9)" role="img" aria-label="Photo of three business people standing together"></div>
    <div class="card-body"><p class="card-meta"><b>By Milo</b> &nbsp;•&nbsp; January 2021</p><h3 class="post-title">Some blog heading<br>goes here</h3><p class="card-text">Nisi elit consequat ipsum nec sagittis sem nibh id elit. Duis sed odio sit amet nibh...</p></div>
  </article>
  <article class="card" style="left:477px;top:3215px;width:244px;height:360px">
    <div class="card-media" style="background:linear-gradient(135deg,#9a9c9e,#e2e2e2)" role="img" aria-label="Photo of a woman on the phone at a laptop"></div>
    <div class="card-body"><p class="card-meta"><b>By Milo</b> &nbsp;•&nbsp; January 2021</p><h3 class="post-title">Some blog heading<br>goes here</h3><p class="card-text">Nisi elit consequat ipsum nec sagittis sem nibh id elit. Duis sed odio sit amet nibh...</p></div>
  </article>
  <article class="card" style="left:740px;top:3215px;width:245px;height:360px">
    <div class="card-media" style="background:linear-gradient(135deg,#7c7f83,#d0d1d2)" role="img" aria-label="Photo of coworkers reviewing a laptop screen"></div>
    <div class="card-body"><p class="card-meta"><b>By Milo</b> &nbsp;•&nbsp; January 2021</p><h3 class="post-title">Some blog heading<br>goes here</h3><p class="card-text">Nisi elit consequat ipsum nec sagittis sem nibh id elit. Duis sed odio sit amet nibh...</p></div>
  </article>
</section>

<!-- contact form -->
<section class="contact">
  <h2 class="h2 abs" style="left:0;top:3658px;width:1200px;text-align:center;font-size:31px">Get in touch with us</h2>
  <span class="label" style="left:293px;top:3722px">NAME*</span>
  <span class="label" style="left:501px;top:3722px">EMAIL*</span>
  <span class="label" style="left:708px;top:3722px">PHONE NUMBER*</span>
  <div class="field" style="left:293px;top:3744px;width:199px;height:48px">Enter your name</div>
  <div class="field" style="left:501px;top:3744px;width:198px;height:48px">Enter your email</div>
  <div class="field" style="left:708px;top:3744px;width:199px;height:48px">Enter your number</div>
  <span class="label" style="left:293px;top:3808px">MESSAGE*</span>
  <div class="field" style="left:293px;top:3830px;width:614px;height:136px;align-items:flex-start;padding-top:16px">Type your text...</div>
  <a class="btn" href="#" style="left:542px;top:3992px;width:116px;height:38px;background:var(--dark);font-size:15px">Send</a>
</section>

<!-- footer -->
<svg class="abs" style="left:0;top:4130px" width="1200" height="685" viewBox="0 0 1200 685">
  <path d="M0,40 C200,20 400,90 650,60 C850,35 1000,20 1200,60 L1200,685 L0,685 Z" fill="var(--footer)"/>
</svg>
<section class="cta abs" style="left:88px;top:4112px;width:1022px;height:200px;background:var(--blue);border-radius:6px">
  <p class="abs" style="left:112px;top:58px;font-size:30px;font-weight:700;line-height:34px;color:var(--white)">Need a Tailor-Made Solution Propel<br>Your Business Into the Heart 2021?<br>Let's Discuss.</p>
  <a class="btn" href="#" style="left:783px;top:80px;width:129px;height:41px;background:var(--white);color:var(--ink)">Contact us</a>
</section>

<footer>
  <div class="abs" style="left:88px;top:4548px;display:flex;align-items:center;gap:10px;font-size:26px;font-weight:600;color:var(--white);letter-spacing:.5px"><span style="width:16px;height:16px;background:var(--blue)"></span>BRIGHT CORRIDOR</div>

  <h4 class="foot-h" style="left:402px;top:4465px">Quick Links</h4>
  <ul class="foot-list" style="left:402px;top:4508px">
    <li>Home</li><li>About Us</li><li>Services</li><li>Our Key Features</li><li>Projects</li><li>Case Studies</li><li>Contact Us</li>
  </ul>

  <h4 class="foot-h" style="left:594px;top:4465px">Contact Info</h4>
  <svg class="abs" style="left:594px;top:4522px" width="14" height="12" viewBox="0 0 14 12"><rect x="1" y="1" width="12" height="10" rx="1" fill="var(--blue)"/><path d="M1,2 L7,7 L13,2" stroke="#fff" stroke-width="1.2" fill="none"/></svg>
  <p class="foot-text" style="left:618px;top:4516px">Email:<br>hello@brightcorridor.test</p>
  <svg class="abs" style="left:594px;top:4584px" width="14" height="14" viewBox="0 0 14 14"><path d="M3,1 L5.5,1 L6.5,4 L5,5.5 C6,7.5 6.5,8 8.5,9 L10,7.5 L13,8.5 L13,11 C13,12 12,13 11,13 C5.5,12.5 1.5,8.5 1,3 C1,2 2,1 3,1 Z" fill="var(--blue)"/></svg>
  <p class="foot-text" style="left:618px;top:4578px">Phone:<br>555-014-2290</p>
  <svg class="abs" style="left:596px;top:4642px" width="12" height="16" viewBox="0 0 12 16"><path d="M6,0 C2.7,0 0,2.6 0,5.8 C0,10 6,16 6,16 C6,16 12,10 12,5.8 C12,2.6 9.3,0 6,0 Z" fill="var(--blue)"/><circle cx="6" cy="6" r="2.2" fill="var(--footer)"/></svg>
  <p class="foot-text" style="left:618px;top:4640px">Office Location:<br>Some address line goes here</p>

  <h4 class="foot-h" style="left:850px;top:4465px">Newsletter</h4>
  <p class="foot-text" style="left:850px;top:4510px;width:240px;font-size:11.5px;line-height:17px">Subscribe to our email address to get the latest news.</p>
  <div class="abs" style="left:850px;top:4570px;width:260px;height:41px;border-radius:21px;background:var(--white);font-size:11px;color:var(--ink);display:flex;align-items:center;padding-left:36px">Enter Your Email...</div>
  <div class="abs" style="left:1068px;top:4570px;width:42px;height:41px;border-radius:0 21px 21px 0;background:var(--blue)">
    <svg width="42" height="41" viewBox="0 0 42 41"><path d="M13,20 L29,13 L24,29 L21,22 Z" fill="#fff"/></svg>
  </div>
  <span class="social" style="left:853px"></span>
  <span class="social" style="left:894px"></span>
  <span class="social" style="left:937px"></span>
  <span class="social" style="left:978px"></span>

  <p class="bottom-bar" style="left:88px">© COPYRIGHT 2021 &nbsp; | &nbsp; ALL RIGHTS RESERVED</p>
  <p class="bottom-bar" style="left:652px;display:flex;gap:20px;font-weight:400"><a href="#">Legal information</a><a href="#">Data protection (GDPR)</a><a href="#">Website owner declaration</a></p>
  <a class="abs" href="#" style="left:1134px;top:4740px;width:34px;height:34px;border-radius:50%;background:var(--white);display:flex;align-items:center;justify-content:center">
    <svg width="12" height="14" viewBox="0 0 12 14"><path d="M6,13 L6,2 M2,6 L6,2 L10,6" stroke="var(--ink)" stroke-width="1.6" fill="none"/></svg>
  </a>
</footer>

</body>
</html>
```